VelmiTaro 16 pages booklet CD Cover

I need a cover (also formatted to be used for digital release), a 16 Pages Booklet + Inlay both sides, a back cover, and a CD image for french pop-rock album.

The name of the artist : Velmitaro
The name of the album : Marcher sous la brume (which means "walking under the mist")
Style of music: I've attached some mp3 extracts. In a few words, this is electro POP music, I'm inspired by band such as The Haze, etc..

This album talks about the desire to live elsewhere, in a world more just and equitable, less painful. The songs talk about people fighting to find a job, to feed their son, poeple who would like to have enough money to enjoy life, etc... but as they can't, at least, they dream about a new world, they draw this elsewhere, hence the title of the album "Marcher sous la brume"

Font styles to use
Sans Serif

Colors
b768aa
33a6d7

Requirements
Must have
• COver: fell free to make your porposal as long as it match the project description objectoves.
• I have add/attached a document "CD Cover Structure" that explains the stucture of the cover, and how i think it could be setup. BUt any other proposal will be welcome.
• For the last one, we will put the song titles and i will let you make me some suggestions.
Nice to have
• the songs are rather melancholy (but not sad) and it would be nice to transmit this impression by the colors. That's why i have chose the pink and blue as primary colours.

```html
<!DOCTYPE html>
<html lang="fr">
<head>
<meta charset="utf-8">
<title>Figer le temps – livret</title>
<link rel="stylesheet" href="https://fonts.googleapis.com/css2?family=Montserrat+Alternates:wght@400;600&family=Cabin:wght@400&display=swap">
<style>
  :root{
    --page-bg:#0d1426;
    --ink:#f2f2f0;
    --chord:#d9a531;
    --teal-a:#6fd6c9;
    --teal-b:#3fb3c8;
    --teal-c:#a9dde8;
    --lime-a:#e4e88a;
    --lime-b:#b8e4c8;
    --lime-c:#7fd3dc;
  }
  html,body{margin:0;padding:0;width:1200px;height:1200px;overflow:hidden;background:var(--page-bg);}
  .page{position:relative;width:1200px;height:1200px;overflow:hidden;background:var(--page-bg);font-family:"Cabin",sans-serif;color:var(--ink);}
  .art{position:absolute;top:0;height:1200px;}
  .art--left{left:0;width:210px;
    background:linear-gradient(170deg,var(--teal-a) 0%,var(--teal-c) 30%,var(--teal-b) 60%,var(--teal-c) 85%,var(--teal-a) 100%);
    clip-path:polygon(0 0,100% 0,97% 8%,99% 17%,96% 29%,98% 41%,95% 55%,97% 68%,94% 80%,97% 91%,96% 100%,0 100%);}
  .art--right{right:0;width:215px;
    background:linear-gradient(180deg,var(--lime-a) 0%,var(--lime-b) 35%,var(--lime-c) 70%,var(--teal-c) 100%);
    clip-path:polygon(4% 0,100% 0,100% 100%,3% 100%,5% 88%,2% 74%,5% 60%,3% 46%,6% 32%,3% 18%);}
  .heading{position:absolute;left:0;top:32px;width:1200px;text-align:center;font-family:"Montserrat Alternates",sans-serif;}
  .heading__title{margin:0;font-size:50px;font-weight:600;line-height:1.1;letter-spacing:1px;}
  .heading__dedication{margin:2px 0 0;font-size:22px;font-weight:400;}
  .heading__author{margin:18px 0 0;font-size:17px;font-weight:400;letter-spacing:.5px;}
  .verses{position:absolute;top:202px;width:450px;margin:0;padding:0;list-style:none;}
  .verses--left{left:170px;}
  .verses--right{left:572px;}
  .line{position:relative;height:41.4px;}
  .chord{position:absolute;top:0;line-height:20px;font-size:15px;color:var(--chord);white-space:nowrap;}
  .lyric{position:absolute;top:18px;left:0;width:100%;line-height:24px;font-size:19.5px;text-align:center;white-space:nowrap;}
</style>
</head>
<body>
<div class="page">
  <div class="art art--left" role="img" aria-label="Peinture abstraite turquoise avec éclaboussures de paillettes dorées"></div>
  <div class="art art--right" role="img" aria-label="Peinture abstraite jaune et turquoise avec éclaboussures de paillettes dorées"></div>

  <header class="heading">
    <h1 class="heading__title">Figer le temps</h1>
    <p class="heading__dedication">(à mon fils qui grandit trop vite)</p>
    <p class="heading__author">(Paul Morvane-Velmitaro)</p>
  </header>

  <ul class="verses verses--left">
    <li class="line"><span class="chord" style="left:101px">D</span><span class="chord" style="left:121px">E</span><span class="chord" style="left:227px">F#m</span><span class="chord" style="left:292px">A</span><span class="lyric">À chacun de tes sourires</span></li>
    <li class="line"><span class="chord" style="left:101px">D</span><span class="chord" style="left:121px">E</span><span class="chord" style="left:251px">F#m</span><span class="chord" style="left:307px">A</span><span class="lyric">À ta main qu’il faut tenir</span></li>
    <li class="line"><span class="chord" style="left:177px">D</span><span class="chord" style="left:336px">E</span><span class="lyric">Quand les soucis loin du sol s’envolent</span></li>
    <li class="line"><span class="chord" style="left:105px">F#m</span><span class="lyric">À chaque jour ses parfums,</span></li>
    <li class="line"><span class="chord" style="left:116px">F#m</span><span class="lyric">Ces découvertes sans fin</span></li>
    <li class="line"><span class="chord" style="left:204px">D</span><span class="lyric">Je garde en moi ces instants</span></li>
    <li class="line"><span class="chord" style="left:214px">E</span><span class="lyric">Comme un défi au temps</span></li>
    <li class="line"><span class="chord" style="left:145px">F#m</span><span class="lyric">La candeur comme un drapeau</span></li>
    <li class="line"><span class="chord" style="left:145px">F#m</span><span class="lyric">La candeur comme un drapeau</span></li>
    <li class="line"></li>
    <li class="line"><span class="chord" style="left:71px">D</span><span class="chord" style="left:91px">E</span><span class="chord" style="left:245px">F#m</span><span class="chord" style="left:341px">A</span><span class="lyric">Les mots qui viendront trop tôt</span></li>
    <li class="line"><span class="chord" style="left:87px">D</span><span class="chord" style="left:107px">E</span><span class="chord" style="left:261px">F#m</span><span class="chord" style="left:313px">A</span><span class="lyric">Prendre leur part du gâteau</span></li>
    <li class="line"><span class="chord" style="left:189px">D</span><span class="lyric">Grignoter l’innocence</span></li>
    <li class="line"><span class="chord" style="left:180px">E</span><span class="lyric">Préparer ton absence</span></li>
    <li class="line"><span class="chord" style="left:97px">D</span><span class="lyric">Graver les rires et les larmes</span></li>
    <li class="line"><span class="chord" style="left:97px">E</span><span class="lyric">Rester transi sous le charme</span></li>
    <li class="line"><span class="chord" style="left:102px">F#m</span><span class="lyric">Petit nez sous nos mentons</span></li>
    <li class="line"><span class="chord" style="left:123px">A</span><span class="lyric">Savoir qu’il s’enfuit à tâtons</span></li>
    <li class="line"><span class="chord" style="left:167px">D</span><span class="lyric">Je voudrais figer le temps</span></li>
    <li class="line"><span class="chord" style="left:182px">E</span><span class="lyric">Oui je voudrais figer le temps</span></li>
    <li class="line"><span class="chord" style="left:188px">F#m</span><span class="lyric">Saisir la lune et les vents</span></li>
    <li class="line"><span class="chord" style="left:169px">F#m</span><span class="lyric">Et s’allonger dans cet instant</span></li>
    <li class="line"><span class="chord" style="left:274px">D</span><span class="chord" style="left:314px">E</span><span class="chord" style="left:331px">F#m</span><span class="chord" style="left:376px">A</span><span class="lyric">Oui dans cet instant</span></li>
  </ul>

  <ul class="verses verses--right">
    <li class="line"><span class="chord" style="left:113px">D</span><span class="chord" style="left:201px">E</span><span class="lyric">Arrêter le temps l’espace</span></li>
    <li class="line"><span class="chord" style="left:118px">F#m</span><span class="chord" style="left:265px">A</span><span class="lyric">Et les traces qui passent</span></li>
    <li class="line"><span class="chord" style="left:113px">D</span><span class="chord" style="left:201px">E</span><span class="lyric">Arrêter le temps l’espace</span></li>
    <li class="line"><span class="chord" style="left:118px">F#m</span><span class="chord" style="left:265px">A</span><span class="lyric">Et les traces qui passent</span></li>
    <li class="line"><span class="chord" style="left:105px">D</span><span class="lyric">Petit nez sous nos mentons</span></li>
    <li class="line"><span class="chord" style="left:125px">E</span><span class="lyric">Savoir qu’il s’enfuit à tâtons</span></li>
    <li class="line"><span class="chord" style="left:169px">D</span><span class="lyric">Je voudrais figer le temps</span></li>
    <li class="line"><span class="chord" style="left:184px">E</span><span class="lyric">Oui je voudrais figer le temps</span></li>
    <li class="line"><span class="chord" style="left:191px">F#m</span><span class="lyric">Saisir la lune et les vents</span></li>
    <li class="line"><span class="chord" style="left:178px">F#m</span><span class="lyric">Et s’allonger dans cet instant</span></li>
    <li class="line"><span class="chord" style="left:169px">D</span><span class="lyric">Je voudrais figer le temps</span></li>
    <li class="line"><span class="chord" style="left:184px">E</span><span class="lyric">Oui je voudrais figer le temps</span></li>
    <li class="line"><span class="chord" style="left:166px">F#m</span><span class="lyric">Le suspendre à ce sourire,</span></li>
    <li class="line"><span class="chord" style="left:204px">A</span><span class="lyric">Et qu’aujourd’hui soit l’avenir.</span></li>
    <li class="line"><span class="chord" style="left:270px">E</span><span class="lyric">Oui soit l’avenir</span></li>
    <li class="line"><span class="chord" style="left:256px">D</span><span class="lyric">Je voudrais garder un bout d’éternité</span></li>
    <li class="line"><span class="chord" style="left:183px">A</span><span class="lyric">Le mettre sous scellé, protégé</span></li>
    <li class="line"><span class="chord" style="left:179px">A</span><span class="lyric">Je veux continuer la danse</span></li>
    <li class="line"><span class="chord" style="left:268px">E</span><span class="lyric">Et graver ta confiance</span></li>
    <li class="line"><span class="chord" style="left:207px">D</span><span class="lyric">Dans l’infini plonger à jamais</span></li>
    <li class="line"><span class="chord" style="left:258px">A</span><span class="lyric">Oh mon petit Théo</span></li>
    <li class="line"><span class="chord" style="left:258px">E</span><span class="lyric">Oh mon petit Théo</span></li>
    <li class="line"><span class="chord" style="left:305px">D</span><span class="chord" style="left:325px">E</span><span class="chord" style="left:342px">F#m</span><span class="chord" style="left:387px">A</span><span class="lyric">Oh mon petit Théo</span></li>
  </ul>
</div>
</body>
</html>
```